Maple Ridge business card design

Card needs to include the following text/items:
Company Logo
Tobin Marsh
Phone # - 555-318-7642
service@mapleridgelandscaping.example
Lawn & landscape maintenance services

```html
<!DOCTYPE html>
<html lang="en">
<head>
<meta charset="utf-8">
<title>Maple Ridge Landscaping – Business Cards</title>
<link rel="stylesheet" href="https://fonts.googleapis.com/css2?family=Cinzel:wght@600&family=Montserrat:wght@400;600;700&display=swap">
<style>
  :root{
    --stage:#7b7a76;
    --page:#ffffff;
    --forest:#1f4a2a;
    --olive:#7f9a33;
    --ink:#2b2b2b;
    --mist-top:#fbfbf7;
    --mist-mid:#eef0df;
    --mist-low:#e3e8c9;
    --grass-dark:#3e7a1f;
    --grass-light:#6fae2f;
    --bush:#2f5a1c;
    --rule:#7f9a33;
  }
  *{margin:0;padding:0;box-sizing:border-box}
  html,body{width:1200px;height:2643px;overflow:hidden;background:var(--page)}
  body{position:relative;font-family:"Montserrat",sans-serif;color:var(--forest)}

  .stage{position:absolute;left:0;top:0;width:1200px;height:900px;background:var(--stage)}

  .card{position:absolute;width:420px;height:734px;overflow:hidden;
    box-shadow:0 6px 14px rgba(0,0,0,.25);}
  .card--mini{transform:scale(.738);transform-origin:top left}

  .card__backdrop{position:absolute;inset:0;
    background:linear-gradient(180deg,var(--mist-top) 0%,var(--mist-mid) 45%,var(--mist-low) 70%,#dfe6c0 100%)}
  .card__field{position:absolute;left:0;right:0;bottom:0;
    background:linear-gradient(180deg,rgba(47,90,28,0) 0%,var(--bush) 22%,#5a4a3a 58%,var(--grass-dark) 64%,var(--grass-light) 100%)}
  .card--front .card__field{height:230px}
  .card--back .card__field{height:170px}

  .brand{position:absolute;left:0;right:0;text-align:center}
  .brand__circle{display:block;margin:0 auto;border-radius:50%;
    border:3px solid var(--olive);background:radial-gradient(circle at 50% 40%,#ffffff,#eef3dc)}
  .brand__name{display:block;font-family:"Cinzel",serif;font-weight:600;color:var(--forest);
    letter-spacing:.5px;line-height:1}

  .card--front .brand{top:52px}
  .card--front .brand__circle{width:190px;height:190px}
  .card--front .brand__name{font-size:44px;margin-top:18px}
  .card--back .brand{top:38px}
  .card--back .brand__circle{width:150px;height:150px}
  .card--back .brand__name{font-size:35px;margin-top:14px}

  .service{position:absolute;left:0;right:0;text-align:center;line-height:1}
  .service__lead{display:block;font-weight:400;color:var(--olive);font-size:31px;letter-spacing:.3px}
  .service__sub{display:block;font-weight:700;color:var(--forest);font-size:20px;margin-top:4px}
  .card--front .service{top:343px}
  .card--back .service{top:238px}

  .web{position:absolute;left:0;right:0;text-align:center;font-size:15px;color:var(--ink)}
  .web b{font-weight:700;color:var(--forest)}
  .card--front .web{top:455px}

  .person{position:absolute;left:0;right:0;top:338px;text-align:center;line-height:1}
  .person__name{font-size:30px;color:var(--forest);letter-spacing:.5px}
  .person__name b{font-weight:700}
  .person__name span{font-weight:400}
  .person__role{display:block;margin-top:6px;font-size:15px;letter-spacing:8px;color:var(--olive);padding-left:8px}
  .person__rule{display:block;width:36px;height:2px;background:var(--olive);margin:12px auto 0}

  .contact{position:absolute;left:60px;right:48px;top:418px;list-style:none;font-size:14.5px;color:var(--ink)}
  .contact li{display:flex;align-items:center;gap:10px;height:26px;border-bottom:1px solid var(--rule)}
  .contact li:last-child{border-bottom:1px solid var(--rule)}
  .contact .phone{font-weight:700;color:var(--ink)}
  .contact b{font-weight:700;color:var(--forest)}
  .contact svg{flex:none;width:16px;height:16px}
</style>
</head>
<body>

<div class="stage"></div>

<!-- front card, small -->
<div class="card card--front card--mini" style="left:247px;top:194px">
  <div class="card__backdrop" role="img" aria-label="Soft misty photo of a countryside path with a white fence"></div>
  <div class="card__field" role="img" aria-label="Photo of a round green bush, wooden fence and lawn"></div>
  <div class="brand"><span class="brand__circle"></span><span class="brand__name">Maple Ridge</span></div>
  <div class="service"><span class="service__lead">LAWN &amp; LANDSCAPE</span><span class="service__sub">• MAINTENANCE SERVICES •</span></div>
  <p class="web">www.<b>mapleridgelandscaping</b>.example</p>
</div>

<!-- back card, small -->
<div class="card card--back card--mini" style="left:643px;top:165px">
  <div class="card__backdrop" role="img" aria-label="Soft misty photo of a countryside path with a white fence"></div>
  <div class="card__field" role="img" aria-label="Photo of a wooden fence, round green bush and lawn"></div>
  <div class="brand"><span class="brand__circle"></span><span class="brand__name">Maple Ridge</span></div>
  <div class="service"><span class="service__lead">LAWN &amp; LANDSCAPE</span><span class="service__sub">• MAINTENANCE SERVICES •</span></div>
  <div class="person"><span class="person__name"><b>TOBIN</b> <span>MARSH</span></span><span class="person__role">OWNER</span><span class="person__rule"></span></div>
  <ul class="contact">
    <li><svg viewBox="0 0 16 16"><path d="M4 2l2.5 3-1.5 1.5a8 8 0 004.5 4.5L11 9.5l3 2.5-1.5 2C7 14 2 9 2 3.5z" fill="none" stroke="#7f9a33" stroke-width="1.4"/></svg><span class="phone">555-318-7642</span></li>
    <li><svg viewBox="0 0 16 16"><rect x="1.5" y="3.5" width="13" height="9" fill="#7f9a33"/><path d="M1.5 3.5l6.5 5 6.5-5" fill="none" stroke="#fff" stroke-width="1.2"/></svg><span>service@mapleridgelandscaping.example</span></li>
    <li><svg viewBox="0 0 16 16"><circle cx="8" cy="8" r="6.3" fill="none" stroke="#7f9a33" stroke-width="1.4"/><path d="M1.7 8h12.6M8 1.7c-3 3.5-3 9 0 12.6M8 1.7c3 3.5 3 9 0 12.6" fill="none" stroke="#7f9a33" stroke-width="1.1"/></svg><span>www.<b>mapleridgelandscaping</b>.example</span></li>
  </ul>
</div>

<!-- front card, full size -->
<div class="card card--front" style="left:390px;top:1004px">
  <div class="card__backdrop" role="img" aria-label="Soft misty photo of a countryside path with a white fence"></div>
  <div class="card__field" role="img" aria-label="Photo of a round green bush, wooden fence and lawn"></div>
  <div class="brand"><span class="brand__circle"></span><span class="brand__name">Maple Ridge</span></div>
  <div class="service"><span class="service__lead">LAWN &amp; LANDSCAPE</span><span class="service__sub">• MAINTENANCE SERVICES •</span></div>
  <p class="web">www.<b>mapleridgelandscaping</b>.example</p>
</div>

<!-- back card, full size -->
<div class="card card--back" style="left:390px;top:1817px">
  <div class="card__backdrop" role="img" aria-label="Soft misty photo of a countryside path with a white fence"></div>
  <div class="card__field" role="img" aria-label="Photo of a wooden fence, round green bush and lawn"></div>
  <div class="brand"><span class="brand__circle"></span><span class="brand__name">Maple Ridge</span></div>
  <div class="service"><span class="service__lead">LAWN &amp; LANDSCAPE</span><span class="service__sub">• MAINTENANCE SERVICES •</span></div>
  <div class="person"><span class="person__name"><b>TOBIN</b> <span>MARSH</span></span><span class="person__role">OWNER</span><span class="person__rule"></span></div>
  <ul class="contact">
    <li><svg viewBox="0 0 16 16"><path d="M4 2l2.5 3-1.5 1.5a8 8 0 004.5 4.5L11 9.5l3 2.5-1.5 2C7 14 2 9 2 3.5z" fill="none" stroke="#7f9a33" stroke-width="1.4"/></svg><span class="phone">555-318-7642</span></li>
    <li><svg viewBox="0 0 16 16"><rect x="1.5" y="3.5" width="13" height="9" fill="#7f9a33"/><path d="M1.5 3.5l6.5 5 6.5-5" fill="none" stroke="#fff" stroke-width="1.2"/></svg><span>service@mapleridgelandscaping.example</span></li>
    <li><svg viewBox="0 0 16 16"><circle cx="8" cy="8" r="6.3" fill="none" stroke="#7f9a33" stroke-width="1.4"/><path d="M1.7 8h12.6M8 1.7c-3 3.5-3 9 0 12.6M8 1.7c3 3.5 3 9 0 12.6" fill="none" stroke="#7f9a33" stroke-width="1.1"/></svg><span>www.<b>mapleridgelandscaping</b>.example</span></li>
  </ul>
</div>

</body>
</html>
```